Holistic Psychologist needs contemporary business card

I am a psychologist working with adult clients face to face and online. The card needs to work for clients and also referring doctors and medical professionals. It needs to look warm, safe and trustable for clients, but clean and professional enough for doctors. Sometimes I also work in a corporate context.

I am holistic in my approach (mind-body-spirit) so anything conveying connection or integration or wholeness would be good. But again, clean and contemporary please. It can have a little bit of personality.
New logo uploaded.

Probably warm tones and plenty white space to write on one side.

My web pages:
http://mkcounsel.com.au
https://www.facebook.com/MarionKellerCounselling?ref=hl
Updates

Hi Designers .. I have decided I do need a new logo before finalising a design for the business cards.  I hope to have this available in 4 days from now.

Kindly,

Marion

New logo now posted, same brief.  Balance of masculine and feminine elements, plenty of white space on one side please.

Keen to see some card designs, thank-you.

Target Market(s)

Audience 1 - Males and females aged 25 years + seeking counselling or coaching. Audience 2 - doctors and health professionals who refer clients.

Industry/Entity Type

Medical

Contact Information for Business Card

Logo

Marion Keller
Registered Psychologist

M: 0491 582 034
www.mkcounsel.com.au
marion@mkcounsel.com.au
Little blue Facebook icon, with "marion keller counselling" printed near it.

Font styles to use
Sans Serif

Requirements
Nice to have
• You might want to play with the words "essential you"
Should not have
• Nothing cutesy or too literal

```html
<!DOCTYPE html>
<html lang="en">
<head>
<meta charset="utf-8">
<title>Marion Keller Psychology – Business Card</title>
<link href="https://fonts.googleapis.com/css2?family=Questrial&display=swap" rel="stylesheet">
<style>
  :root {
    --backdrop: #dcdcdc;
    --card: #ffffff;
    --card-shade: #f2f2f2;
    --brand-red: #e0282b;
    --ink: #2b2b2b;
    --ink-soft: #555555;
    --rule: #2e2e2e;
    --social-blue: #4a7cc4;
  }
  * { box-sizing: border-box; margin: 0; padding: 0; }
  html, body {
    width: 1200px; height: 900px; overflow: hidden;
    background: var(--backdrop);
    font-family: "Questrial", "Helvetica Neue", Arial, sans-serif;
  }
  .canvas {
    position: relative; width: 1200px; height: 900px;
    display: flex; align-items: center; justify-content: center; gap: 40px;
  }
  .card {
    position: relative; width: 540px; height: 309px;
    background: var(--card);
    box-shadow: 0 10px 28px rgba(0,0,0,0.18);
  }
  .brand {
    display: flex; align-items: center; gap: 12px;
    color: var(--brand-red);
  }
  .brand-dot {
    width: 30px; height: 30px; border-radius: 50%;
    background: var(--brand-red); flex: none;
  }
  .brand-name { font-size: 30px; letter-spacing: 0.5px; white-space: nowrap; }

  .card-front { display: flex; align-items: center; justify-content: center; }

  .card-back {
    background: linear-gradient(to bottom, var(--card) 0%, var(--card) 45%, var(--card-shade) 100%);
  }
  .card-back .brand { position: absolute; top: 44px; left: 0; right: 0; justify-content: center; }
  .card-back .brand-name { font-size: 26px; }
  .card-back .brand-dot { width: 26px; height: 26px; }
  .divider {
    position: absolute; top: 128px; left: 0; right: 0;
    height: 5px; background: var(--rule);
  }
  .holder { position: absolute; left: 30px; top: 168px; }
  .holder-name { font-size: 21px; letter-spacing: 3px; color: var(--ink); }
  .holder-title { font-size: 10px; letter-spacing: 2.4px; color: var(--brand-red); margin-top: 4px; }

  .contacts {
    position: absolute; left: 270px; top: 162px;
    list-style: none; display: flex; flex-direction: column; gap: 7px;
  }
  .contact { display: flex; align-items: center; gap: 9px; font-size: 14px; letter-spacing: 2px; color: var(--ink); }
  .contact-icon {
    width: 20px; height: 20px; border-radius: 3px; background: var(--brand-red);
    display: flex; align-items: center; justify-content: center; flex: none;
  }
  .contact-icon svg { width: 14px; height: 14px; }
  .contact-social { color: var(--social-blue); }
  .contact-social .contact-icon { background: var(--social-blue); }
</style>
</head>
<body>
<main class="canvas">
  <section class="card card-front" aria-label="Card front">
    <div class="brand">
      <span class="brand-dot"></span>
      <span class="brand-name">Marion Keller Psychology</span>
    </div>
  </section>

  <section class="card card-back" aria-label="Card back">
    <div class="brand">
      <span class="brand-dot"></span>
      <span class="brand-name">Marion Keller Psychology</span>
    </div>
    <div class="divider"></div>

    <div class="holder">
      <p class="holder-name">Marion Keller</p>
      <p class="holder-title">REGISTERED PSYCHOLOGIST</p>
    </div>

    <ul class="contacts">
      <li class="contact">
        <span class="contact-icon">
          <svg viewBox="0 0 14 14"><rect x="4" y="1" width="6" height="12" rx="1" fill="none" stroke="#fff" stroke-width="1.4"/><line x1="6" y1="11" x2="8" y2="11" stroke="#fff" stroke-width="1.2"/></svg>
        </span>
        <span>0491 582 034</span>
      </li>
      <li class="contact">
        <span class="contact-icon">
          <svg viewBox="0 0 14 14"><rect x="1.5" y="3.5" width="11" height="7.5" fill="none" stroke="#fff" stroke-width="1.3"/><polyline points="1.5,3.5 7,8 12.5,3.5" fill="none" stroke="#fff" stroke-width="1.3"/></svg>
        </span>
        <span>marion@mkcounsel.com.au</span>
      </li>
      <li class="contact">
        <span class="contact-icon">
          <svg viewBox="0 0 14 14"><circle cx="7" cy="7" r="5.5" fill="none" stroke="#fff" stroke-width="1.2"/><ellipse cx="7" cy="7" rx="2.4" ry="5.5" fill="none" stroke="#fff" stroke-width="1"/><line x1="1.5" y1="7" x2="12.5" y2="7" stroke="#fff" stroke-width="1"/></svg>
        </span>
        <span>www.mkcounsel.com.au</span>
      </li>
      <li class="contact contact-social">
        <span class="contact-icon"></span>
        <span>marion keller counselling</span>
      </li>
    </ul>
  </section>
</main>
</body>
</html>
```